Onboarding Infographic/brochure

We are a small criminal defense firm looking to create some sort of infographic or brochure that we can onboard new clients with. We are currently sending it out via email but want something a bit cooler and fun to send to clients. The information is:

A Few Quick Rules

We are here to help each step of the way. While questions are never discouraged, this letter will answer some of the most common ones we get asked.

Communications

As a client, you should always be in the loop. While we will try to respond to questions as quickly as possible, sometimes we are unable to respond right away. Do not worry - we promise to get back to you soon. Some questions might take some time to research, and a correct answer is better than a quick one.

Appointments

One of the benefits of having an attorney is the ability to discuss your case outside of court, minus the stress and headaches. If you need an appointment, please contact the office.

Appointments must be scheduled in advance. We do not want you to make a special trip to the office only to learn that we are in court or otherwise unavailable.

Jail Visits

If your family member is currently in jail, we take that very seriously. We will visit your loved one and introduce ourselves. While the case is ongoing, we ask that a family member be designated a “contact” person so that messages can be relayed quickly. Never discuss the facts of the case over the phone with someone who is in jail. Jail calls are recorded and we have seen too many cases go south based on remarks made over recorded lines.

Police Reports and Discovery

We will do our best to provide you with copies of everything we receive on your case. Most information will be emailed, so please keep your email address up to date.

Changes in Contact Information

If you move or change numbers during the case, please let us know. It is difficult to help if we are unable to reach you, and helping you is why we are here.

Court Appearances

Cases do not get resolved as quickly as they do on television. Expect there to be several hearings in your case and it may be necessary for you to attend one or more of them. If a hearing is set, you will receive notice of the date and time of each hearing.

Billing and Collections

We understand that this investment was a huge decision for you. As we focus on providing the best representation, we will need for you to stay on schedule with any payment arrangements agreed to at the time of your initial consultation.

Again, thank you for your trust in us. We look forward to getting a fantastic outcome on your case.

Target Market(s)

Criminal defense clients and their families

Industry/Entity Type

Legal

Font styles to use
Serif

Requirements
Must have
• Must incorporate all of the rules we email out. Would like diagrams, images or pictures
Nice to have
• We attached a Welcome brochure. Not sure I want it to look super similar, hence the request for infographic.

```html
<!DOCTYPE html>
<html lang="en">
<head>
<meta charset="utf-8">
<title>A Few Quick Rules – Harlow Legal Group</title>
<link href="https://fonts.googleapis.com/css2?family=Montserrat:wght@400;500;700&display=swap" rel="stylesheet">
<style>
  :root{
    --paper:#f4f7f6;
    --ink:#3d4446;
    --slate:#4b5357;
    --footer:#2b3032;
    --blue:#0d36ff;
    --teal:#1a6e73;
    --gold:#c48a10;
    --red:#e0103c;
    --violet:#6a0aff;
    --orange:#f25207;
    --card:#f7f9f9;
  }
  *{margin:0;padding:0;box-sizing:border-box}
  html,body{width:988px;height:1200px;overflow:hidden;background:var(--paper)}
  body{font-family:"Montserrat",Arial,sans-serif;color:var(--ink);position:relative}
  .title{position:absolute;left:63px;top:60px;font-size:28px;font-weight:700;color:var(--slate);letter-spacing:-.2px}
  .title .mark{background:var(--slate);color:#fff;padding:0 4px 1px 4px}
  .intro{position:absolute;left:63px;top:104px;width:880px;font-size:20.5px;line-height:23px;color:var(--ink)}
  .rule{position:absolute;border:1.2px dashed var(--c);border-radius:34px}
  .rule .band{position:absolute;inset:15px 13px;background:var(--c);border-radius:24px}
  .rule .sheet{position:absolute;inset:31px 26px 31px 26px;background:var(--card);border-radius:11px;box-shadow:0 3px 4px rgba(0,0,0,.18)}
  .rule h2{position:absolute;left:16px;top:6px;font-size:19px;line-height:22px;font-weight:700;color:var(--c);white-space:nowrap}
  .rule p{position:absolute;left:33px;font-size:13.5px;line-height:15px;color:var(--ink);white-space:nowrap}
  .rule .icon{position:absolute;right:12px;top:11px;width:34px;height:34px;color:var(--c)}
  .icon svg{width:100%;height:100%;fill:none;stroke:currentColor;stroke-width:1.6;stroke-linecap:round;stroke-linejoin:round}
  .closing{position:absolute;left:63px;top:1072px;width:880px;font-size:20.5px;line-height:23px}
  .footer{position:absolute;left:0;right:0;bottom:0;height:60px;background:var(--footer);color:#fff;font-weight:700;font-size:13.5px}
  .footer .site{position:absolute;left:63px;top:23px}
  .footer .firm{position:absolute;right:63px;top:21px;font-size:14.5px;display:flex;align-items:center;gap:6px}
  .footer .firm .dot{width:12px;height:12px;background:#2f9bff}
</style>
</head>
<body>
  <h1 class="title">A Few <span class="mark">Quick Rules</span></h1>
  <p class="intro">We are here to help each step of the way. While questions are never discouraged, this letter will answer some of the most common ones we get asked.</p>

  <section class="rule" style="--c:var(--blue);left:63px;top:170px;width:423px;height:234px">
    <div class="band"></div>
    <div class="sheet">
      <h2>Communications</h2>
      <div class="icon" style="width:46px;right:10px"><svg viewBox="0 0 46 34"><path d="M3 4h22a2 2 0 0 1 2 2v10a2 2 0 0 1-2 2H12l-5 4v-4H3a2 2 0 0 1-2-2V6a2 2 0 0 1 2-2z"/><path d="M20 13h22a2 2 0 0 1 2 2v8a2 2 0 0 1-2 2h-4v5l-5-5H20a2 2 0 0 1-2-2v-8a2 2 0 0 1 2-2z"/><path d="M9 11h1M13 11h1M17 11h1M24 18h14M26 21h10"/></svg></div>
      <p style="top:42px">As a client, you should always be in the<br>loop. While we will try to respond to<br>questions as quickly as possible, sometimes<br>we are unable to respond right away. Do not<br>worry - we promise to get back to you soon.<br>Some questions might take some time to<br>research, and a correct answer is better than<br>a quick one.</p>
    </div>
  </section>

  <section class="rule" style="--c:var(--gold);left:63px;top:420px;width:423px;height:293px">
    <div class="band"></div>
    <div class="sheet">
      <h2>Jail Visits</h2>
      <div class="icon"><svg viewBox="0 0 34 34"><rect x="1" y="1" width="32" height="32"/><path d="M17 1v10M10 11h14M6 19h22M9 19v12M25 19v12M13 15v16M21 15v16"/></svg></div>
      <p style="top:43px">If your family member is currently in jail,<br>we take that very seriously. We will visit your<br>loved one and introduce ourselves. While the<br>case is ongoing, we ask that a family member<br>be designated a “contact” person so that<br>messages can be relayed quickly.</p>
      <p style="top:148px">Never discuss the facts of the case over the<br>phone with someone who is in jail. Jail calls<br>are recorded and we have seen too many<br>cases go south based on remarks made over<br>recorded lines.</p>
    </div>
  </section>

  <section class="rule" style="--c:var(--slate);left:63px;top:728px;width:423px;height:205px">
    <div class="band"></div>
    <div class="sheet">
      <h2>Court Appearances</h2>
      <div class="icon"><svg viewBox="0 0 34 34"><path d="M2 10L17 2l15 8zM4 10v20M30 10v20M1 31h32M8 14h18v14H8zM17 15v11M12 18h10M12 18l-2 5h4zM22 18l-2 5h4z"/><circle cx="17" cy="6.5" r="1.5"/></svg></div>
      <p style="top:43px">Cases do not get resolved as quickly as<br>they do on television. Expect there to be<br>several hearings in your case and it may be<br>necessary for you to attend one or more of<br>them. If a hearing is set, you will receive notice<br>of the date and time of each hearing.</p>
    </div>
  </section>

  <section class="rule" style="--c:var(--teal);left:501px;top:170px;width:425px;height:264px">
    <div class="band"></div>
    <div class="sheet">
      <h2>Appointments</h2>
      <div class="icon"><svg viewBox="0 0 34 34"><rect x="1" y="4" width="28" height="27"/><path d="M1 10h28M7 1v6M23 1v6M6 15h2M12 15h2M18 15h2M24 15h2M6 20h2M12 20h2M18 20h2M6 25h2M12 25h2"/><circle cx="27" cy="27" r="6" fill="var(--card)"/><path d="M27 24v3h2"/></svg></div>
      <p style="top:42px">One of the benefits of having an<br>attorney is the ability to discuss your<br>case outside of court, minus the stress and<br>headaches. If you need an appointment,<br>please contact the office.</p>
      <p style="top:132px">Appointments must be scheduled in advance.<br>We do not want you to make a special trip to<br>the office only to learn that we are in court or<br>otherwise unavailable.</p>
    </div>
  </section>

  <section class="rule" style="--c:var(--red);left:501px;top:449px;width:425px;height:175px">
    <div class="band"></div>
    <div class="sheet">
      <h2>Police Reports and Discovery</h2>
      <div class="icon"><svg viewBox="0 0 34 34"><rect x="1" y="1" width="28" height="32"/><rect x="5" y="5" width="20" height="24"/><path d="M29 6h3v3h-3M29 13h3v3h-3M15 8l5 2v4c0 3-2 5-5 6-3-1-5-3-5-6v-4zM10 23h10v4H10z"/></svg></div>
      <p style="top:42px">We will do our best to provide you with<br>copies of everything we receive on your case.<br>Most information will be emailed, so please<br>keep your email address up to date.</p>
    </div>
  </section>

  <section class="rule" style="--c:var(--violet);left:501px;top:639px;width:425px;height:196px">
    <div class="band"></div>
    <div class="sheet">
      <h2>Changes in Contact<br>Information</h2>
      <div class="icon"><svg viewBox="0 0 34 34"><rect x="1" y="3" width="32" height="28" rx="2"/><path d="M1 8h32"/><circle cx="10" cy="16" r="3"/><path d="M4 26c1-4 3-5 6-5s5 1 6 5zM19 14h10M19 19h10M19 24h10"/></svg></div>
      <p style="top:64px">If you move or change numbers during the case,<br>please let us know. It is difficult to help if we are<br>unable to reach you, and helping you is why we<br>are here.</p>
    </div>
  </section>

  <section class="rule" style="--c:var(--orange);left:501px;top:851px;width:425px;height:204px">
    <div class="band"></div>
    <div class="sheet">
      <h2 style="left:20px">Billing and Collections</h2>
      <div class="icon"><svg viewBox="0 0 34 34"><path d="M5 12h18v18H2v-4h3zM23 30a3 3 0 0 0 3-3V17M9 17h10M9 21h10M9 25h6"/><circle cx="26" cy="8" r="7" fill="var(--card)"/><path d="M28 5h-3a1.5 1.5 0 0 0 0 3h2a1.5 1.5 0 0 1 0 3h-3M26 3.5v1.5M26 11v1.5"/></svg></div>
      <p style="top:42px;left:37px">We understand that this investment was<br>a huge decision for you. As we focus on<br>providing the best representation, we will need<br>for you to stay on schedule with any payment<br>arrangements agreed to at the time of your<br>initial consultation.</p>
    </div>
  </section>

  <p class="closing">Again, thank you for your trust in us. We look forward to getting a fantastic outcome on your case.</p>

  <footer class="footer">
    <span class="site">WWW.HARLOWLEGALGROUP.COM</span>
    <span class="firm"><span class="dot"></span>HARLOW LEGAL GROUP</span>
  </footer>
</body>
</html>
```